TELVANO End User Instruction Guide

I need to create a 5 to 7-page instruction guides for customers who purchased a phone system from our company. The document is a quick reference guide that will help end-users learn how to set up and use their new desk phone and software applications. I need the guide to be 3 x 5 or 6 x 8 in size and will fold like a book.

Target Market(s)

Business users / Corvana Desk Phone Users / TelVANO Portal users

Industry/Entity Type

Telecommunications

Font styles to use
Serif

Colors
0758a5
ffffff

Requirements
Must have
• Need to have step-by-step instructions that include the information from the QuickStart guide I provided. I need to see an image of the phone with an arrow pointing to the key on the phone that should be pressed. For example, when checking voicemail the Messages key is pressed and I want to highlight this button or call it out somehow.

I need to have three pages for setup instructions, one page for shortcuts or features codes and our support contacts on the last page.
Nice to have
• I want to have a page for notes that the end-user can use during training. I would also like to have a blank space next to passwords and user ID's so they can be filled out with specific details that are provided during their training. For example, in the voicemail section, I include a default PIN. I would like to leave this blank and let the end-user fill it out during training.
Should not have
• Complex shapes and designs. I like straight lines and a simple easy to understand layout.

```html
<!DOCTYPE html>
<html lang="en">
<head>
<meta charset="utf-8">
<title>TelVANO Guide – Voicemail</title>
<link rel="stylesheet" href="https://fonts.googleapis.com/css2?family=Roboto:ital,wght@0,400;0,500;0,700;1,400&family=Roboto+Condensed:wght@500;700&display=swap">
<style>
:root{
  --ink:#1d1d1f;
  --blue:#1f4e9a;
  --navy:#2a3c5e;
  --slate:#33424f;
  --line:#2e4f8c;
  --paper:#ffffff;
  --grey:#8b8f94;
}
*{box-sizing:border-box;margin:0;padding:0}
html,body{width:1200px;height:800px;overflow:hidden;background:var(--paper)}
body{position:relative;font-family:"Roboto",sans-serif;color:var(--ink)}
.abs{position:absolute}
.brand{position:absolute;top:36px;display:flex;align-items:center;gap:7px;font-family:"Roboto",sans-serif;font-weight:700;color:var(--slate)}
.brand .sq{width:22px;height:22px;background:var(--slate)}
.brand .name{font-size:23px;letter-spacing:1px;line-height:1}
.brand .sub{font-size:7px;letter-spacing:3.2px;font-weight:500;display:block;margin-top:2px}
.rail{position:absolute;background:var(--navy)}
.step-tab{position:absolute;left:82px;top:102px;width:112px;height:47px;background:var(--slate);clip-path:polygon(0 0,93% 0,100% 100%,0 100%);color:#fff;font-family:"Roboto",sans-serif;font-weight:700;font-size:29px;padding:6px 0 0 4px}
.page-title{position:absolute;left:195px;top:91px;width:366px;text-align:center;color:var(--blue);font-size:27px;line-height:30px;font-weight:400}
.heading{position:absolute;font-family:"Roboto Condensed",sans-serif;font-weight:500;color:var(--blue);font-size:19.5px;line-height:1;white-space:nowrap}
.heading.big{font-size:20px}
.sub{position:absolute;font-style:italic;text-decoration:underline;font-size:16.5px;line-height:1;white-space:nowrap}
ol.steps{position:absolute;list-style:none;font-size:14px;line-height:16.7px}
ol.steps li{position:relative;padding-left:24px;margin-bottom:5.5px}
ol.steps li .n{position:absolute;left:0;top:0;width:16px;height:16px;border-radius:50%;background:var(--navy);color:#fff;font-size:11.5px;line-height:16px;text-align:center}
b.key{color:var(--blue);font-weight:500}
.para{position:absolute;font-size:14px;line-height:16.7px}
ul.dots{position:absolute;list-style:none;font-size:14px;line-height:16.7px}
ul.dots li{position:relative;padding-left:12px;margin-bottom:8px}
ul.dots li::before{content:"";position:absolute;left:1px;top:5px;width:6px;height:6px;border-radius:50%;background:var(--navy)}
.link{color:var(--blue)}
.login{position:absolute;left:1019px;top:225px;width:118px;height:98px;border:1px solid #9aa;background:#fff;font-size:6px;padding:6px 5px}
.login .lbl{font-weight:700;margin-bottom:3px}
.login .field{height:13px;border:1px solid #ccc;font-size:5.5px;padding:3px;margin-bottom:6px}
.login .field.on{border-color:#7aa6d8}
.login .btn{margin:9px auto 0;width:57px;height:19px;background:#a3283f;color:#fff;border-radius:2px;text-align:center;line-height:19px;font-size:7px;font-weight:700}
.portal{position:absolute;left:754px;top:492px;width:385px;height:152px;border:1px solid #888;background:#fff;font-size:5px;color:#444}
.toolbar{display:flex;gap:7px;padding:9px 0 0 26px}
.tool{width:30px;text-align:center;font-size:4.5px;color:#888}
.tool i{display:block;width:30px;height:23px;border-radius:4px;background:linear-gradient(#c8ccd0,#8d959c);margin-bottom:2px}
.tool.on i{background:linear-gradient(#8fc3ef,#3f86cc)}
.bar{margin:12px 3px 0;height:12px;background:linear-gradient(#b8bcc0,#8a9096);color:#fff;font-weight:700;font-size:6.5px;padding:2px 4px}
.tabs{margin:6px 6px 0;border-bottom:1px solid #ddd;display:flex;gap:10px;padding:2px 6px;font-size:5px}
.tabs span:last-child{color:var(--blue)}
.sel{margin:8px 0 0 8px;width:56px;height:10px;border:1px solid #bbb;font-size:5px;font-weight:700;padding:2px 4px}
table.msgs{margin:7px 6px 0 8px;width:370px;border-collapse:collapse;font-size:4.8px}
table.msgs th{font-weight:700;text-align:left;padding:1px}
table.msgs td{border-top:1px solid #e2e2e2;padding:3px 1px}
table.msgs td.num{color:var(--blue)}
</style>
</head>
<body>
<div class="brand" style="left:33px"><span class="sq"></span><span><span class="name">TELVANO</span><span class="sub">COMMUNICATIONS</span></span></div>
<div class="brand" style="left:990px"><span class="sq"></span><span><span class="name">TELVANO</span><span class="sub">COMMUNICATIONS</span></span></div>

<div class="rail" style="left:76px;top:75px;width:6px;height:725px"></div>
<div class="rail" style="left:1129px;top:75px;width:6px;height:725px"></div>
<div class="rail" style="left:0;top:762px;width:599px;height:6px;background:var(--slate)"></div>
<div class="rail" style="left:603px;top:762px;width:597px;height:6px;background:var(--slate)"></div>

<svg class="abs" style="left:0;top:0" width="1200" height="800" aria-hidden="true">
  <g stroke="#2e4f8c" stroke-width="1.3" fill="#fff">
    <line x1="82" y1="186" x2="180" y2="186"/><circle cx="183" cy="186" r="3"/>
    <line x1="82" y1="535" x2="320" y2="535"/><circle cx="323" cy="535" r="3"/>
    <line x1="1011" y1="98" x2="1129" y2="98"/><circle cx="1008" cy="98" r="3"/>
    <line x1="751" y1="335" x2="1129" y2="335"/><circle cx="748" cy="335" r="3"/>
  </g>
</svg>

<div class="step-tab">Step 1</div>
<h1 class="page-title">Create your personal voicemail greeting</h1>

<h2 class="heading" style="left:193px;top:177px">Accessing Voicemail from your desk phone</h2>
<h3 class="sub" style="left:135px;top:216px">To access voicemail</h3>
<ol class="steps" style="left:139px;top:252px;width:410px">
  <li><span class="n">1</span>Press the <b class="key">Messages</b> button on your phone to access your voicemail box, or dial 5001 if you can not identify the voicemail button.</li>
  <li><span class="n">2</span>If you subscribe to multiple mailboxes, a list of mailboxes may appear. Select the mail box you want to access.</li>
  <li><span class="n">3</span>When prompted, enter your default voicemail pin 2323, and then press #.</li>
</ol>
<h3 class="sub" style="left:135px;top:403px">To access another person’s mailbox</h3>
<ol class="steps" style="left:139px;top:440px;width:410px">
  <li><span class="n">1</span>Dial <b class="key">5000</b>.</li>
  <li><span class="n">2</span>When prompted, enter the other person’s extension number.</li>
  <li><span class="n">3</span>Enter the voicemail PIN of the other person’s mailbox, followed by #.</li>
</ol>
<h2 class="heading" style="left:345px;top:526px">Setting Up Your Mailbox</h2>
<p class="para" style="left:135px;top:560px;width:410px">The first time you log in to your mailbox you are walked through recording your name for the directory and recording your personal greeting. The name recording is for the dial-by-name directory, so when someone enters the first three letters of your last name, it will play back your name recording.</p>
<p class="para" style="left:135px;top:660px;width:410px">The greeting plays when your mailbox is reached. It is very important to make a custom message, as many callers will not leave messages at mailboxes that have generic greetings.</p>

<h2 class="heading big" style="left:653px;top:88px">Accessing Voicemail from the user portal</h2>
<h3 class="sub" style="left:653px;top:127px">To access the web portal</h3>
<ol class="steps" style="left:657px;top:163px;width:420px">
  <li><span class="n">1</span>Start a web browser.</li>
  <li><span class="n">2</span>Go to phone <span class="link">telvanocommunications.com</span></li>
</ol>
<ul class="dots" style="left:676px;top:206px;width:340px">
  <li>Click in the Login name field and type ext@customerdomain. Your customerdomain typically is the same as your email address domain.</li>
  <li>Click in the Password field and enter your user password. (default password is Welcome01).</li>
</ul>
<div class="login">
  <div class="lbl">Login Name</div><div class="field">111@customerdomain.com</div>
  <div class="lbl">Password</div><div class="field on">●●●●●●</div>
  <div class="btn">Log In</div>
</div>

<h2 class="heading big" style="left:653px;top:325px">Voicemail</h2>
<p class="para" style="left:653px;top:361px;width:440px">You configure voicemail using the Messages page. This page has two tabs for handling voicemail.</p>
<ul class="dots" style="left:676px;top:398px;width:420px">
  <li><b class="key">Messages</b> — see "Messages" below.</li>
  <li><b class="key">Settings</b> — see "<b class="key">Settings tab</b>" on the next page.</li>
</ul>
<p class="para" style="left:653px;top:463px;width:450px">To display the Messages page, click the <b class="key">Messages</b> icon at the top of the page:</p>

<div class="portal">
  <div class="toolbar">
    <div class="tool"><i></i>Home</div><div class="tool on"><i></i>Messages</div><div class="tool"><i></i>Fax</div><div class="tool"><i></i>Contacts</div><div class="tool"><i></i>Answering Rules</div><div class="tool"><i></i>Time Frames</div><div class="tool"><i></i>Phones</div><div class="tool"><i></i>Music on Hold</div><div class="tool"><i></i>Reporting</div>
  </div>
  <div class="bar">Messages</div>
  <div class="tabs"><span>Voicemail</span><span>Settings</span></div>
  <div class="sel">New ▾</div>
  <table class="msgs">
    <tr><th></th><th>From</th><th>Date</th><th>Duration</th></tr>
    <tr><td class="num">▶ (555) 010-2417</td><td>LARSEN MAREN</td><td>Feb 11th 11:05 am</td><td>0:35</td></tr>
    <tr><td class="num">▶ (555) 010-8830</td><td>Oakdale Line</td><td>Feb 6th 10:54 am</td><td>0:10</td></tr>
    <tr><td class="num">▶ (555) 010-6152</td><td>BRENTFIELD</td><td>Feb 4th 8:50 am</td><td>0:11</td></tr>
  </table>
</div>

<h3 class="sub" style="left:653px;top:660px">To record a greeting</h3>
<ol class="steps" style="left:657px;top:687px;width:440px">
  <li><span class="n">3</span>From the <b class="key">Settings</b> tab of the Messages page, click the speaker icon</li>
  <li><span class="n">4</span>Next to <b class="key">New Greeting</b>, click <b class="key">Record</b> and the system will call you, or upload an existing greeting.</li>
</ol>
</body>
</html>
```